Boat business cards

I'm looking for business cards with the two logos I've attached. I don't have an specific idea in mind and open to anything. All the usual info will be on the card. Name, position in company, nr, email, address, ect. The company rents out these two boats for charters and fishing.

```html
<!DOCTYPE html>
<html lang="en">
<head>
<meta charset="utf-8">
<title>Harbor Tide – Business Cards</title>
<link rel="stylesheet" href="https://fonts.googleapis.com/css2?family=Montserrat:wght@400;500;700&display=swap">
<style>
  :root {
    --page-bg: #ffffff;
    --blue-deep: #0a3f9e;
    --blue-mid: #0658c8;
    --blue-bright: #0a72dc;
    --blue-sky: #0fa2ea;
    --panel-light: #b6d4f1;
    --panel-edge: #b0c8ea;
    --ink: #111111;
    --white: #ffffff;
  }
  * { margin: 0; padding: 0; box-sizing: border-box; }
  html, body {
    width: 1200px; height: 1200px; overflow: hidden;
    background: var(--page-bg);
    font-family: "Montserrat", sans-serif;
  }
  .canvas { position: relative; width: 1200px; height: 1200px; }

  .card { position: absolute; overflow: hidden; }
  .card-pattern { position: absolute; inset: 0; }

  /* Front */
  .card-front { left: 239px; top: 170px; width: 699px; height: 409px; }
  .card-front .card-pattern {
    background:
      radial-gradient(ellipse 45% 60% at 85% 8%, rgba(255,255,255,0.16), transparent 70%),
      radial-gradient(ellipse 40% 50% at 10% 95%, rgba(255,255,255,0.12), transparent 70%),
      linear-gradient(135deg, var(--blue-bright) 0%, var(--blue-mid) 50%, var(--blue-deep) 100%);
  }
  .brand-small {
    position: absolute; left: 41px; top: 52px;
    display: flex; align-items: center; gap: 8px;
    font-weight: 700; font-size: 18px; color: var(--white); letter-spacing: 0.5px;
  }
  .brand-mark {
    width: 22px; height: 22px; border-radius: 50%;
    background: var(--white);
  }
  .person { position: absolute; right: 51px; top: 36px; text-align: right; color: var(--white); }
  .person-name { font-weight: 700; font-size: 24px; line-height: 1; }
  .person-role { font-weight: 400; font-size: 18px; margin-top: 6px; }

  .info-panel {
    position: absolute; left: 0; top: 111px; width: 100%; height: 246px;
    background: linear-gradient(90deg, var(--panel-light) 0%, var(--panel-light) 60%, var(--panel-edge) 100%);
    opacity: 0.95;
  }
  .contact-list { position: absolute; left: 41px; top: 240px; list-style: none; }
  .contact-list li {
    display: flex; align-items: center; height: 27px;
    font-size: 17.5px; font-weight: 500; color: var(--ink);
  }
  .contact-list svg { width: 22px; height: 22px; margin-right: 8px; fill: var(--ink); flex: none; }

  .front-footer {
    position: absolute; left: 41px; right: 51px; top: 360px;
    display: flex; justify-content: space-between; align-items: center;
    color: var(--white); font-size: 17.5px; font-weight: 500;
  }
  .footer-item { display: flex; align-items: center; }
  .footer-item svg { width: 22px; height: 22px; margin-right: 8px; flex: none; }

  /* Back */
  .card-back { left: 233px; top: 628px; width: 711px; height: 417px; }
  .card-back .card-pattern {
    background:
      radial-gradient(ellipse 40% 45% at 5% 10%, rgba(255,255,255,0.14), transparent 70%),
      radial-gradient(ellipse 30% 40% at 95% 40%, rgba(255,255,255,0.08), transparent 70%),
      linear-gradient(135deg, var(--blue-sky) 0%, var(--blue-bright) 30%, var(--blue-mid) 55%, var(--blue-deep) 100%);
  }
  .brand-large {
    position: absolute; left: 0; right: 0; top: 208px;
    display: flex; justify-content: center; align-items: center; gap: 14px;
    font-weight: 700; font-size: 40px; color: var(--white); letter-spacing: 1px;
  }
  .brand-large .brand-mark { width: 44px; height: 44px; }
</style>
</head>
<body>
<div class="canvas">

  <section class="card card-front" aria-label="Business card front">
    <div class="card-pattern" role="img" aria-label="Faceted blue geometric background pattern"></div>
    <div class="brand-small"><span class="brand-mark"></span>Harbor Tide</div>
    <div class="person">
      <div class="person-name">Xxxxx Xxxxx</div>
      <div class="person-role">Xxxxxx</div>
    </div>
    <div class="info-panel"></div>
    <ul class="contact-list">
      <li><svg viewBox="0 0 24 24"><path d="M12 1a7 7 0 0 0-7 7c0 5 7 15 7 15s7-10 7-15a7 7 0 0 0-7-7zm0 9.5A2.5 2.5 0 1 1 12 5.5a2.5 2.5 0 0 1 0 5z"/></svg>: xxxxxxxxxxxxxxxxxxx</li>
      <li><svg viewBox="0 0 24 24"><path d="M6.6 10.8a15 15 0 0 0 6.6 6.6l2.2-2.2a1 1 0 0 1 1-.25 11 11 0 0 0 3.6.6 1 1 0 0 1 1 1V20a1 1 0 0 1-1 1A17 17 0 0 1 3 4a1 1 0 0 1 1-1h3.5a1 1 0 0 1 1 1c0 1.25.2 2.45.6 3.6a1 1 0 0 1-.25 1z"/></svg>: xxx-xxx-xxxx</li>
      <li><svg viewBox="0 0 24 24"><path d="M8 1h8a2 2 0 0 1 2 2v18a2 2 0 0 1-2 2H8a2 2 0 0 1-2-2V3a2 2 0 0 1 2-2zm0 3v14h8V4zm4 15.5a1 1 0 1 0 0 2 1 1 0 0 0 0-2z"/></svg>: xxx-xxx-xxxx</li>
      <li><svg viewBox="0 0 24 24"><path d="M1 4h22v16H1zm2 2v.5l9 6.5 9-6.5V6zm0 3v9h18V9l-9 6.5z"/></svg>: xxxxxx@xxxxxxxxx.xxx</li>
    </ul>
    <div class="front-footer">
      <div class="footer-item">
        <svg viewBox="0 0 24 24" fill="var(--white)"><path d="M1 4h22v16H1zm2 2v.5l9 6.5 9-6.5V6zm0 3v9h18V9l-9 6.5z"/></svg>: xxxxxx@xxxxxxxxx.xxx
      </div>
      <div class="footer-item">
        <svg viewBox="0 0 24 24" fill="none" stroke="var(--white)" stroke-width="1.6"><circle cx="12" cy="12" r="10"/><ellipse cx="12" cy="12" rx="4.5" ry="10"/><path d="M2 12h20M4 6.5h16M4 17.5h16M12 2v20"/></svg>: www.xxxxxxxxxxxxxxx.xxx
      </div>
    </div>
  </section>

  <section class="card card-back" aria-label="Business card back">
    <div class="card-pattern" role="img" aria-label="Faceted blue geometric background pattern"></div>
    <div class="brand-large"><span class="brand-mark"></span>Harbor Tide</div>
  </section>

</div>
</body>
</html>
```